Website for Brisbeck Current Glide

Require a website for a river float in the City of Edmonton. Located on North Saskatchewan River. Will need to be a coded website with incorporated booking system through Fare Harbor software.

Pages include
Home
Pricing
About
FAQ
Contact

Brisbeck Current Glide is an activity based business that will have customers floating down the North Saskatchewan river in Edmonton AB. The site will have all information needed and a full reservation system. The project was launched to provide people in the Edmonton area a favorite summer activity.

Here are similar websites to reference what our business will be doing and what we are looking for.

mellowbendcanoehire.example
pinegulchloopers.example

Target Market(s)

Families, Groups, Individuals, Anyone who wants to explore the river

Industry/Entity Type

Activities based business/ Outdoor recreational/ River Float

Coding

Coded - Design and coding required

Number of Pages Required

5+ page

Colors
0054AA
0677BA
7BADD7
CADEEF
E8F1F8
F0912C
F2A743
F7CA91
FBE8D2
FDF5EE

```html
<!DOCTYPE html>
<html lang="en">
<head>
<meta charset="utf-8">
<title>Brisbeck Current Glide</title>
<link href="https://fonts.googleapis.com/css2?family=Montserrat:wght@400;500;600;700;800&display=swap" rel="stylesheet">
<style>
:root{
  --blue:#0054AA;--ocean:#0677BA;--sky:#7BADD7;--mist:#CADEEF;--foam:#E8F1F8;
  --orange:#F0912C;--amber:#F2A743;--peach:#F7CA91;--navy:#0b2c6b;--cyan:#4cc6ea;
  --ink:#2b2b2b;--white:#fff;
}
*{margin:0;padding:0;box-sizing:border-box}
html,body{width:1200px;height:3978px;overflow:hidden}
body{font-family:'Montserrat',sans-serif;color:var(--ink);background:var(--white)}
.page{position:relative;width:1200px;height:3978px;overflow:hidden}
.abs{position:absolute}
.btn{position:absolute;display:flex;align-items:center;justify-content:center;background:var(--orange);color:var(--white);font-weight:700;font-size:18px;letter-spacing:.5px;border-radius:28px;text-decoration:none}

/* header */
.site-header{position:absolute;left:0;top:0;width:1200px;height:108px;background:var(--white);z-index:5}
.brand-badge{position:absolute;left:65px;top:-16px;width:201px;height:201px;border-radius:50%;background:var(--white);z-index:6;display:flex;align-items:center;justify-content:center;text-align:center;padding:40px 20px 0}
.brand-badge span{font-weight:800;font-size:19px;line-height:1.15;color:var(--navy)}
.main-nav a{position:absolute;top:49px;font-size:16px;font-weight:700;color:#222;text-decoration:none}
.main-nav a.active{color:var(--orange)}

/* hero */
.hero-photo{left:0;top:108px;width:1200px;height:710px;background:linear-gradient(180deg,#b9bcbd 0%,#8e9690 28%,#6b7657 48%,#5a6040 62%,#3f4536 78%,#2f3a36 100%)}
.hero-title{left:0;width:1200px;top:322px;text-align:center;color:var(--white);font-weight:700;font-size:62px;letter-spacing:.5px;text-shadow:0 2px 6px rgba(0,0,0,.35)}
.hero-sub{left:0;width:1200px;top:400px;text-align:center;color:var(--white);font-weight:700;font-size:24px;text-shadow:0 2px 5px rgba(0,0,0,.45)}
.dots{left:567px;top:690px;display:flex;gap:10px}
.dots i{display:block;width:14px;height:14px;border-radius:50%;background:var(--white)}
.dots i.on{background:var(--cyan)}

/* about */
.about-ring{left:92px;top:911px;width:495px;height:495px;border-radius:50%;background:var(--cyan)}
.about-photo{left:77px;top:911px;width:486px;height:486px;border-radius:50%;border:5px solid var(--foam);background:radial-gradient(circle at 45% 40%,#7d8f8a 0%,#4f6461 45%,#2e3f40 100%)}
.about-title{left:616px;top:945px;font-size:46px;font-weight:800;line-height:1.02;color:var(--navy);letter-spacing:.5px}
.about-tag{left:616px;top:1060px;font-size:20px;font-weight:600;line-height:1.4;color:var(--orange)}
.about-copy{left:616px;top:1155px;width:520px;font-size:15px;line-height:27.5px;color:#333}

/* pricing */
.pricing-photo{left:0;top:1500px;width:1200px;height:708px;background:linear-gradient(100deg,#4e6a2e 0%,#7a8a3a 25%,#a28a3a 45%,#6f7a34 65%,#3d5a2c 85%,#2f4a2a 100%)}
.pricing-card{left:74px;top:1647px;width:542px;height:496px;border-radius:14px;background:rgba(6,119,186,.88);color:var(--white)}
.pricing-card h2{position:absolute;left:32px;top:22px;font-size:46px;font-weight:800}
.pricing-card h3{position:absolute;left:34px;top:84px;font-size:25px;font-weight:600}
.pricing-card .intro{position:absolute;left:34px;top:128px;width:420px;font-size:15px;line-height:26px;font-weight:500}
.perk{position:absolute;font-size:15px;font-weight:500;line-height:26px;padding-left:34px}
.perk svg{position:absolute;left:0;top:5px}
.pricing-card .group{position:absolute;left:34px;top:437px;font-size:16px;font-weight:500}
.pricing-card .note{position:absolute;left:34px;top:462px;font-size:13px;color:var(--mist)}

/* faq */
.faq-title{left:0;width:1200px;top:2262px;text-align:center;font-size:46px;font-weight:800;color:var(--navy)}
.faq-item{position:absolute;width:511px;height:52px;border:1.5px solid #d6d6d6;border-radius:3px;display:flex;align-items:center;justify-content:space-between;padding:0 18px 0 16px;font-size:17px;font-weight:500;color:#333}

/* contact */
.contact-photo{left:0;top:2872px;width:1200px;height:707px;background:linear-gradient(180deg,#0b4a8c 0%,#0c3f78 40%,#133f5c 70%,#123a4a 100%)}
.contact-title{left:74px;top:3066px;font-size:46px;font-weight:800;color:var(--white)}
.contact-lead{left:74px;top:3143px;font-size:26px;font-weight:500;color:var(--white)}
.contact-line{position:absolute;left:74px;font-size:20px;font-weight:500;color:var(--white);display:flex;align-items:center;gap:14px}
.contact-line .ic{width:24px;display:flex;justify-content:center}
.social-dot{width:24px;height:24px;border-radius:50%;border:2px solid var(--white)}
.visit{left:74px;top:3476px;font-size:18px;font-weight:700;color:var(--white)}
.map-area{left:631px;top:3022px;width:494px;height:494px;border-radius:50%;border:4px solid var(--foam);background:radial-gradient(circle at 45% 40%,#e4f0e4 0%,#e9eee9 60%,#eef0ee 100%)}

/* footer */
.site-footer{left:0;top:3579px;width:1200px;height:327px;background:var(--blue)}
.foot-head{position:absolute;font-size:17px;font-weight:700;color:var(--sky);line-height:25px}
.foot-link{position:absolute;left:74px;font-size:14px;font-weight:700;color:var(--white)}
.foot-text{position:absolute;left:278px;font-size:14px;color:var(--white);display:flex;align-items:center;gap:12px}
.days-badge{left:616px;top:3713px;width:171px;height:101px;border-radius:10px;background:rgba(255,255,255,.18)}
.email-field{left:885px;top:3715px;width:241px;height:47px;border-radius:24px;background:var(--white);font-size:14px;color:#666;display:flex;align-items:center;padding-left:18px}
.subscribe{left:885px;top:3774px;width:241px;height:48px;font-size:16px}
.copyright{left:0;top:3906px;width:1200px;height:72px;background:var(--blue);border-top:1px solid rgba(255,255,255,.25);display:flex;align-items:center;justify-content:center;font-size:14px;color:var(--white)}
</style>
</head>
<body>
<div class="page">

  <header class="site-header">
    <nav class="main-nav">
      <a class="active" style="left:633px">HOME</a>
      <a style="left:731px">PRICING</a>
      <a style="left:851px">ABOUT</a>
      <a style="left:957px">FAQ</a>
      <a style="left:1040px">CONTACT</a>
    </nav>
  </header>
  <div class="brand-badge"><span>BRISBECK<br>CURRENT GLIDE</span></div>

  <section>
    <div class="abs hero-photo" role="img" aria-label="Downtown Edmonton skyline above a bridge over the North Saskatchewan River"></div>
    <h1 class="abs hero-title">BRISBECK CURRENT GLIDE</h1>
    <p class="abs hero-sub">Float the North Saskatchewan through downtown Edmonton</p>
    <a class="btn" style="left:496px;top:457px;width:208px;height:54px">BOOK NOW</a>
    <div class="abs dots"><i class="on"></i><i></i><i></i></div>
    <svg class="abs" style="left:0;top:690px" width="1200" height="130" viewBox="0 0 1200 130" aria-hidden="true">
      <path d="M0 40 C180 10 330 30 480 55 C640 80 760 20 900 30 C1040 40 1120 60 1200 45 L1200 130 L0 130Z" fill="#0677BA" opacity=".85"/>
      <path d="M0 60 C150 45 260 70 420 80 C560 88 700 55 860 58 C1000 60 1100 80 1200 70 L1200 130 L0 130Z" fill="#7BADD7" opacity=".9"/>
      <path d="M0 85 C140 110 300 118 460 108 C620 98 760 72 920 78 C1060 84 1140 100 1200 96 L1200 130 L0 130Z" fill="#ffffff"/>
    </svg>
  </section>

  <section>
    <div class="abs about-ring"></div>
    <div class="abs about-photo" role="img" aria-label="Group of friends relaxing on river tubes"></div>
    <h2 class="abs about-title">ABOUT BRISBECK<br>CURRENT GLIDE</h2>
    <p class="abs about-tag">Float the North Saskatchewan through<br>downtown Edmonton<br>Edmonton’s Best Summer Activity</p>
    <p class="abs about-copy">We provide the lifejacket, paddle, river tube and shuttle service. You just have to show up. Brisbeck Current Glide was launched to provide people in the Edmonton area a favorite summer activity. Nothing is better on a hot summer day, than spending it on the river and seeing Edmonton from a new perspective.</p>
    <a class="btn" style="left:616px;top:1328px;width:207px;height:54px">READ MORE</a>
  </section>

  <section>
    <div class="abs pricing-photo" role="img" aria-label="Woman in a sun hat lounging on an inflatable ring on the water"></div>
    <svg class="abs" style="left:0;top:1490px" width="1200" height="110" viewBox="0 0 1200 110" aria-hidden="true">
      <path d="M0 40 C100 36 220 55 360 62 C500 70 600 58 720 64 C600 80 480 92 340 90 C200 88 90 78 0 82Z" fill="#7BADD7" opacity=".6"/>
      <path d="M700 62 C820 50 920 70 1020 60 C1110 50 1160 30 1200 22 L1200 85 C1120 92 1000 96 880 88 C800 82 750 74 700 62Z" fill="#0054AA" opacity=".7"/>
      <path d="M0 0 H1200 V18 C1120 26 1020 55 900 52 C780 48 690 24 560 30 C420 36 300 56 150 50 C90 48 40 40 0 42Z" fill="#ffffff"/>
    </svg>
    <div class="abs pricing-card">
      <h2>PRICING</h2>
      <h3>Float Tube and Shuttle</h3>
      <p class="intro">We keep our pricing simple and include everything you need:</p>
      <div class="perk" style="left:32px;top:185px;width:310px"><svg width="16" height="16" viewBox="0 0 16 16"><circle cx="8" cy="8" r="8" fill="#fff"/><path d="M4.5 8.2l2.3 2.2 4.7-4.7" stroke="#0677BA" stroke-width="1.8" fill="none"/></svg>Premium comfort float tube with backrest and cup holder</div>
      <div class="perk" style="left:32px;top:248px"><svg width="16" height="16" viewBox="0 0 16 16"><circle cx="8" cy="8" r="8" fill="#fff"/><path d="M4.5 8.2l2.3 2.2 4.7-4.7" stroke="#0677BA" stroke-width="1.8" fill="none"/></svg>Lifejacket</div>
      <div class="perk" style="left:32px;top:286px"><svg width="16" height="16" viewBox="0 0 16 16"><circle cx="8" cy="8" r="8" fill="#fff"/><path d="M4.5 8.2l2.3 2.2 4.7-4.7" stroke="#0677BA" stroke-width="1.8" fill="none"/></svg>Paddle</div>
      <div class="perk" style="left:32px;top:324px"><svg width="16" height="16" viewBox="0 0 16 16"><circle cx="8" cy="8" r="8" fill="#fff"/><path d="M4.5 8.2l2.3 2.2 4.7-4.7" stroke="#0677BA" stroke-width="1.8" fill="none"/></svg>Round trip shuttle service</div>
      <div class="perk" style="left:358px;top:188px"><svg width="16" height="16" viewBox="0 0 16 16"><circle cx="8" cy="8" r="8" fill="#fff"/><path d="M4.5 8.2l2.3 2.2 4.7-4.7" stroke="#0677BA" stroke-width="1.8" fill="none"/></svg>Safety training</div>
      <div class="perk" style="left:358px;top:226px"><svg width="16" height="16" viewBox="0 0 16 16"><circle cx="8" cy="8" r="8" fill="#fff"/><path d="M4.5 8.2l2.3 2.2 4.7-4.7" stroke="#0677BA" stroke-width="1.8" fill="none"/></svg>Staff assistance</div>
      <div class="perk" style="left:358px;top:264px"><svg width="16" height="16" viewBox="0 0 16 16"><circle cx="8" cy="8" r="8" fill="#fff"/><path d="M4.5 8.2l2.3 2.2 4.7-4.7" stroke="#0677BA" stroke-width="1.8" fill="none"/></svg>Parking</div>
      <div class="perk" style="left:358px;top:302px"><svg width="16" height="16" viewBox="0 0 16 16"><circle cx="8" cy="8" r="8" fill="#fff"/><path d="M4.5 8.2l2.3 2.2 4.7-4.7" stroke="#0677BA" stroke-width="1.8" fill="none"/></svg>Unlimited Fun!</div>
      <a class="btn" style="left:32px;top:371px;width:207px;height:54px">BOOK NOW</a>
      <p class="group">Group of 10 or more? Contact us (link to contact)</p>
      <p class="note">*does not include taxes or fees</p>
    </div>
  </section>

  <section>
    <h2 class="abs faq-title">FAQ’S</h2>
    <div class="faq-item" style="left:74px;top:2352px">How do I reserve my float?<svg width="10" height="14" viewBox="0 0 10 14"><path d="M2 2l5 5-5 5" stroke="#222" stroke-width="2" fill="none"/></svg></div>
    <div class="faq-item" style="left:604px;top:2352px">What time should I arrive?<svg width="10" height="14" viewBox="0 0 10 14"><path d="M2 2l5 5-5 5" stroke="#222" stroke-width="2" fill="none"/></svg></div>
    <div class="faq-item" style="left:74px;top:2423px">What safety information should I know?<svg width="10" height="14" viewBox="0 0 10 14"><path d="M2 2l5 5-5 5" stroke="#222" stroke-width="2" fill="none"/></svg></div>
    <div class="faq-item" style="left:604px;top:2423px">Where should I park?<svg width="10" height="14" viewBox="0 0 10 14"><path d="M2 2l5 5-5 5" stroke="#222" stroke-width="2" fill="none"/></svg></div>
    <div class="faq-item" style="left:74px;top:2494px">What is included?<svg width="10" height="14" viewBox="0 0 10 14"><path d="M2 2l5 5-5 5" stroke="#222" stroke-width="2" fill="none"/></svg></div>
    <div class="faq-item" style="left:604px;top:2494px">How long does the trip take?<svg width="10" height="14" viewBox="0 0 10 14"><path d="M2 2l5 5-5 5" stroke="#222" stroke-width="2" fill="none"/></svg></div>
    <div class="faq-item" style="left:74px;top:2565px">What should I bring?<svg width="10" height="14" viewBox="0 0 10 14"><path d="M2 2l5 5-5 5" stroke="#222" stroke-width="2" fill="none"/></svg></div>
    <div class="faq-item" style="left:604px;top:2565px">What happens if I miss my shuttle?<svg width="10" height="14" viewBox="0 0 10 14"><path d="M2 2l5 5-5 5" stroke="#222" stroke-width="2" fill="none"/></svg></div>
    <div class="faq-item" style="left:74px;top:2636px">Where are you located?<svg width="10" height="14" viewBox="0 0 10 14"><path d="M2 2l5 5-5 5" stroke="#222" stroke-width="2" fill="none"/></svg></div>
    <div class="faq-item" style="left:604px;top:2636px">How do I complete the waiver?<svg width="10" height="14" viewBox="0 0 10 14"><path d="M2 2l5 5-5 5" stroke="#222" stroke-width="2" fill="none"/></svg></div>
    <a class="btn" style="left:496px;top:2747px;width:208px;height:54px">VIEW ALL</a>
  </section>

  <section>
    <div class="abs contact-photo" role="img" aria-label="Evening view of the river valley and Edmonton skyline under a blue tint"></div>
    <svg class="abs" style="left:0;top:2862px" width="1200" height="110" viewBox="0 0 1200 110" aria-hidden="true">
      <path d="M0 0 H1200 V30 C1100 12 990 40 880 35 C740 28 640 5 520 15 C380 27 250 50 120 40 C70 36 30 30 0 35Z" fill="#ffffff"/>
      <path d="M0 35 C120 45 250 55 400 45 C520 35 640 20 760 35 C880 50 1000 55 1200 40 L1200 110 L0 110Z" fill="#7BADD7" opacity=".8"/>
      <path d="M0 70 C160 60 320 85 480 80 C640 75 780 55 940 62 C1060 68 1140 75 1200 70 L1200 110 L0 110Z" fill="#0677BA" opacity=".85"/>
    </svg>
    <h2 class="abs contact-title">CONTACT US</h2>
    <p class="abs contact-lead">We’d love to hear from you!</p>
    <div class="contact-line" style="top:3196px"><span class="ic"><svg width="16" height="20" viewBox="0 0 16 20"><path d="M8 1a7 7 0 0 0-7 7c0 5 7 11 7 11s7-6 7-11a7 7 0 0 0-7-7z" fill="#fff"/><circle cx="8" cy="8" r="2.6" fill="#0c3f78"/></svg></span>412 Ferrow Ave NW, Edmonton, AB</div>
    <div class="contact-line" style="top:3237px;gap:10px"><span class="ic" style="width:16px"><svg width="16" height="18" viewBox="0 0 16 18"><path d="M3 1l3 .5 1 4-2 1.5c1 2.5 2.5 4 5 5l1.5-2 4 1 .5 3c-1 1.5-2.5 2-4 1.5C6 14 2 10 1 5 .6 3.5 1.5 2 3 1z" fill="#fff"/></svg></span>780XXXXXXX</div>
    <div class="contact-line" style="top:3275px;gap:10px"><span class="ic" style="width:16px"><svg width="18" height="14" viewBox="0 0 18 14"><rect width="18" height="14" rx="1.5" fill="#fff"/><path d="M1 2l8 6 8-6" stroke="#0c3f78" stroke-width="1.6" fill="none"/></svg></span>info@brisbeckcurrentglide.example</div>
    <div class="contact-line" style="top:3320px;gap:36px"><span class="social-dot"></span>Photo feed</div>
    <div class="contact-line" style="top:3368px;gap:36px"><span class="social-dot"></span>Community page</div>
    <div class="contact-line" style="top:3416px;gap:36px"><span class="social-dot"></span>Review listing</div>
    <p class="abs visit">COME VISIT US ON FLOAT DAYS AT ALDER LANDING</p>
    <div class="abs map-area" role="img" aria-label="Street map showing the launch point near Alder Landing"></div>
  </section>

  <footer>
    <div class="abs site-footer"></div>
    <h4 class="foot-head" style="left:74px;top:3648px">SITE MAP</h4>
    <a class="foot-link" style="top:3692px">HOME</a>
    <a class="foot-link" style="top:3731px">PRICING</a>
    <a class="foot-link" style="top:3769px">ABOUT</a>
    <a class="foot-link" style="top:3808px">FAQ</a>
    <a class="foot-link" style="top:3847px">CONTACT</a>

    <h4 class="foot-head" style="left:278px;top:3648px">CONNECT US</h4>
    <p class="foot-text" style="top:3692px;font-weight:700">BRISBECK CURRENT GLIDE</p>
    <p class="foot-text" style="top:3721px"><svg width="13" height="16" viewBox="0 0 16 20"><path d="M8 1a7 7 0 0 0-7 7c0 5 7 11 7 11s7-6 7-11a7 7 0 0 0-7-7z" fill="#fff"/><circle cx="8" cy="8" r="2.6" fill="#0054AA"/></svg>412 Ferrow Ave NW, Edmonton, AB</p>
    <p class="foot-text" style="top:3754px"><svg width="14" height="11" viewBox="0 0 18 14"><rect width="18" height="14" rx="1.5" fill="#fff"/><path d="M1 2l8 6 8-6" stroke="#0054AA" stroke-width="1.6" fill="none"/></svg>info@brisbeckcurrentglide.example</p>
    <p class="foot-text" style="top:3798px;gap:18px"><span class="social-dot" style="width:18px;height:18px"></span><span class="social-dot" style="width:18px;height:18px"></span><span class="social-dot" style="width:18px;height:18px"></span></p>

    <h4 class="foot-head" style="left:616px;top:3648px">FLOATING 7 DAYS<br>A WEEK</h4>
    <div class="abs days-badge" role="img" aria-label="Open seven days a week badge"></div>

    <h4 class="foot-head" style="left:885px;top:3648px">SIGN UP FOR OUR<br>MAILING LIST</h4>
    <div class="abs email-field">Enter Email</div>
    <a class="btn subscribe">SUBSCRIBE</a>

    <div class="abs copyright">Copyright © 2022. Company Name.&nbsp; All Right Reserved</div>
  </footer>

</div>
</body>
</html>
```